Flyer needed for new essence range

I need flyer to advertise a new essence. It should feature the logo attached and give a brief description of what the essence is about. I would also like a link to the website for further reading. The essence is for balancing the Base chakra. I've also included the label design for the first essence
Updates

Hello everyone. Thank you for all your submissions so far. Please refer to the brief again as I have just updated the text for the flyer. My apologies for any inconvenience. Kind regards, Dario

Target Market(s)

People interested in natural, alternative therapies and spiritual development

Requirements
Must have
• The logo.
A single page or double sided
A6 size
The following text:
"Orvanelle: to stir the quiet; the art of being wholly present"
Orvanelle Base Essence
Foundation, Security, Grounding. Connection to Heart, Body and the Physical world. Reveals “True Nature” and Purpose.
Orvanelle Base Essence has been created to help connect body, mind and heart, revealing a greater sense of self and a renewed sense of purpose. Made in the beautiful Barrington Tops from a combination of herbs, flowers and crystals, it gently dissolves feelings of disconnection, fear and insecurity. People report feeling calm, tranquil, present, grounded and safe, even when they are going through major periods of transition.
"It opens the heart and clears away obstacles to living in an open-hearted way, which is another demonstration of its ability to break apart ‘that which no longer serves"
The recommended dose is 7 drops taken daily for a 3 month period to fully experience all that this wonderful essence has to offer.
Go to orvanelleessences.com.au for the full story.
Nice to have
• A deep red colour. Gold
Should not have
• Green

```html
<!DOCTYPE html>
<html lang="en">
<head>
<meta charset="utf-8">
<title>Orvanelle Essences – Base Essence Flyer</title>
<link href="https://fonts.googleapis.com/css2?family=Cinzel:wght@400;500&family=EB+Garamond:ital,wght@0,400;0,500&display=swap" rel="stylesheet">
<style>
  :root {
    --stage: #ececec;
    --red-light: #c4434c;
    --red: #ad2832;
    --red-deep: #8f1c25;
    --gold-light: #f6d77a;
    --gold: #d9a93a;
    --gold-deep: #a8741c;
    --cream: #fbf1e4;
  }
  * { box-sizing: border-box; margin: 0; padding: 0; }
  html, body {
    width: 1200px; height: 900px; overflow: hidden;
    background: var(--stage);
  }
  .stage {
    width: 1200px; height: 900px;
    display: flex; justify-content: center; align-items: center; gap: 64px;
  }
  .flyer-page {
    position: relative;
    width: 440px; height: 622px;
    background: radial-gradient(ellipse at 40% 35%, var(--red-light) 0%, var(--red) 55%, var(--red-deep) 100%);
    color: var(--cream);
    font-family: "EB Garamond", "Times New Roman", serif;
    display: flex; flex-direction: column; align-items: center;
    box-shadow: 0 10px 30px rgba(0,0,0,0.18);
    overflow: hidden;
  }
  .gold-band {
    position: absolute; left: 0; right: 0; height: 24px;
    background: linear-gradient(90deg, var(--gold-deep), var(--gold-light) 35%, var(--gold) 65%, var(--gold-deep));
  }
  .gold-band--top { top: 0; }
  .gold-band--bottom { bottom: 0; }

  /* Front */
  .brand-mark {
    margin-top: 92px;
    width: 120px; height: 120px;
    border-radius: 50%;
    border: 6px solid var(--gold);
  }
  .brand-name {
    margin-top: 34px;
    font-family: "EB Garamond", "Times New Roman", serif;
    font-weight: 400;
    color: var(--gold);
    text-align: center;
    text-transform: uppercase;
    line-height: 1.1;
  }
  .brand-name__main { display: block; font-size: 52px; letter-spacing: 6px; }
  .brand-name__sub { display: block; font-size: 26px; letter-spacing: 6px; margin-top: 6px; }
  .front-quote {
    margin-top: auto; margin-bottom: 78px;
    font-size: 23px; line-height: 1.25; text-align: center;
    color: #ffffff;
  }

  /* Back */
  .back-title {
    margin-top: 58px;
    font-size: 17px; color: #ffffff;
  }
  .gold-rule {
    width: 360px; height: 1px; margin: 14px 0;
    background: linear-gradient(90deg, transparent, var(--gold-light), transparent);
  }
  .virtues {
    font-size: 17px; line-height: 1.15; text-align: center; color: #ffffff;
  }
  .description {
    width: 372px;
    font-size: 12.4px; line-height: 1.32; text-align: center; color: #ffffff;
  }
  .more-info {
    margin-top: auto; margin-bottom: 58px; text-align: center;
  }
  .more-info__lead { font-size: 15px; color: #ffffff; }
  .more-info__url {
    display: block; margin-top: 8px;
    font-family: "Cinzel", "Times New Roman", serif;
    font-size: 17px; letter-spacing: 0.5px;
    color: var(--gold);
    text-decoration: none;
  }
</style>
</head>
<body>
<main class="stage">

  <section class="flyer-page flyer-page--front" aria-label="Flyer front">
    <div class="gold-band gold-band--top" role="img" aria-label="Gold diamond-pattern border band"></div>
    <div class="brand-mark" aria-hidden="true"></div>
    <h1 class="brand-name">
      <span class="brand-name__main">Orvanelle</span>
      <span class="brand-name__sub">Essences</span>
    </h1>
    <p class="front-quote">“To stir the quiet,<br>The art of being wholly present.”</p>
    <div class="gold-band gold-band--bottom" role="img" aria-label="Gold diamond-pattern border band"></div>
  </section>

  <section class="flyer-page flyer-page--back" aria-label="Flyer back">
    <div class="gold-band gold-band--top" role="img" aria-label="Gold diamond-pattern border band"></div>
    <h2 class="back-title">Orvanelle Base Essence</h2>
    <div class="gold-rule"></div>
    <p class="virtues">Foundation, Security, Grounding.<br>Connection to Heart,<br>Body and the Physical world.<br>Reveals “True Nature” and Purpose.</p>
    <div class="gold-rule"></div>
    <p class="description">Orvanelle Base Essence has been created to help connect body, mind and heart, revealing a greater sense of self and a renewed sense of purpose. Made in the beautiful Barrington Tops from a combination of herbs, flowers and crystals, it gently dissolves feelings of disconnection, fear and insecurity. People report feeling calm, tranquil, present, grounded and safe, even when they are going through major periods of transition. ‘It opens the heart and clears away obstacles to living in an open-hearted way, which is another demonstration of its ability to break apart ‘that which no longer serves’. The recommended dose is 7 drops taken daily for a 3 month period to fully experience all that this wonderful essence has to offer.</p>
    <div class="more-info">
      <p class="more-info__lead">For the full story, go to...</p>
      <a class="more-info__url" href="#">ORVANELLEESSENCES.COM.AU</a>
    </div>
    <div class="gold-band gold-band--bottom" role="img" aria-label="Gold diamond-pattern border band"></div>
  </section>

</main>
</body>
</html>
```